New Business Card Design Project

Hi! I would like for you to design a business card for our aesthetic injections business. We offer Velmo, filler, skin care. I would like it to be elegant, feminine, modern and sleek/clean. I like black/gold foil/ivory/parchment colors. It can be either one or two sided. I would like matte black with gold foil logo on one side and ivory with gold foil information on the other side

Target Market(s)

target market is the discerning woman who wants to look her best

Industry/Entity Type

beauty

Contact Information for Business Card

logo, name, phone, email, website, instagram, facebook, location

Requirements
Must have
• logo and info
Nice to have
• the icons for cell, instagram, email, fb etc
Should not have
• images of people

```html
<!DOCTYPE html>
<html lang="en">
<head>
<meta charset="utf-8">
<title>Velour Lounge — Business Card</title>
<link rel="stylesheet" href="https://fonts.googleapis.com/css2?family=Arimo:wght@400;700&display=swap">
<style>
  :root {
    --backdrop: #2b2b2d;
    --ivory: #fcf3cc;
    --ink: #151515;
    --matte: #1b1c1e;
    --gold: #c9a04a;
  }
  html, body {
    margin: 0;
    width: 1200px;
    height: 1108px;
    overflow: hidden;
    background: var(--backdrop);
    font-family: "Arimo", Arial, sans-serif;
  }
  .stage {
    position: relative;
    width: 1200px;
    height: 1108px;
  }
  .card {
    position: absolute;
    top: 184px;
    width: 420px;
    height: 740px;
    border-radius: 26px;
    box-shadow: 0 18px 40px rgba(0,0,0,.45);
    box-sizing: border-box;
    overflow: hidden;
  }
  .card-front {
    left: 150px;
    background: var(--ivory);
    color: var(--ink);
    text-align: center;
  }
  .card-back {
    left: 630px;
    background: var(--matte);
  }
  .brand-seal {
    position: absolute;
    left: 80px;
    top: 50px;
    width: 260px;
    height: 260px;
    border: 2px solid var(--ink);
    border-radius: 50%;
    display: flex;
    align-items: center;
    justify-content: center;
    box-sizing: border-box;
  }
  .brand-name {
    font-size: 34px;
    font-weight: 400;
    letter-spacing: 2px;
    line-height: 1.15;
    text-transform: uppercase;
  }
  .person {
    position: absolute;
    top: 340px;
    left: 0;
    right: 0;
  }
  .person-name {
    margin: 0;
    font-size: 26px;
    font-weight: 700;
    letter-spacing: .5px;
  }
  .person-role {
    margin: 2px 0 0;
    font-size: 21px;
  }
  .icon-row {
    position: absolute;
    top: 416px;
    left: 40px;
    right: 40px;
    display: flex;
    align-items: center;
    justify-content: center;
    gap: 8px;
  }
  .icon-row .rule {
    flex: 1;
    height: 2px;
    background: var(--ink);
  }
  .icon {
    width: 30px;
    height: 30px;
    border-radius: 50%;
    background: var(--ink);
    display: flex;
    align-items: center;
    justify-content: center;
  }
  .contacts {
    position: absolute;
    top: 464px;
    left: 0;
    right: 0;
    margin: 0;
    padding: 0;
    list-style: none;
    font-size: 22px;
    line-height: 30px;
  }
  .divider {
    position: absolute;
    top: 634px;
    left: 40px;
    right: 40px;
    height: 2px;
    background: var(--ink);
  }
  .address {
    position: absolute;
    top: 648px;
    left: 0;
    right: 0;
    margin: 0;
    font-size: 21px;
    line-height: 26px;
    font-style: normal;
  }
  .back-seal {
    position: absolute;
    left: 140px;
    top: 520px;
    width: 140px;
    height: 140px;
    border: 2px solid var(--gold);
    border-radius: 50%;
    display: flex;
    align-items: center;
    justify-content: center;
    box-sizing: border-box;
  }
  .back-seal .brand-name {
    color: var(--gold);
    font-size: 19px;
    letter-spacing: 1px;
  }
</style>
</head>
<body>
<main class="stage">
  <section class="card card-front" aria-label="Card front">
    <div class="brand-seal">
      <span class="brand-name">Velour<br>Lounge</span>
    </div>

    <div class="person">
      <h1 class="person-name">DANIEL BROOKS</h1>
      <p class="person-role">Manager</p>
    </div>

    <div class="icon-row">
      <span class="rule"></span>
      <span class="icon" aria-label="Phone">
        <svg width="16" height="16" viewBox="0 0 24 24"><path fill="#fcf3cc" d="M6.6 10.8a15.1 15.1 0 0 0 6.6 6.6l2.2-2.2c.3-.3.7-.4 1-.2 1.1.4 2.3.6 3.6.6.6 0 1 .4 1 1V20c0 .6-.4 1-1 1A17 17 0 0 1 3 4c0-.6.4-1 1-1h3.5c.6 0 1 .4 1 1 0 1.3.2 2.5.6 3.6.1.3 0 .7-.2 1z"/></svg>
      </span>
      <span class="icon" aria-label="Email">
        <svg width="16" height="16" viewBox="0 0 24 24"><rect x="2" y="5" width="20" height="14" rx="1.5" fill="none" stroke="#fcf3cc" stroke-width="2"/><path d="M3 6l9 7 9-7" fill="none" stroke="#fcf3cc" stroke-width="2"/></svg>
      </span>
      <span class="icon" aria-label="Website">
        <svg width="16" height="16" viewBox="0 0 24 24" fill="none" stroke="#fcf3cc" stroke-width="2"><circle cx="12" cy="12" r="9"/><path d="M3 12h18M12 3c3 3 3 15 0 18M12 3c-3 3-3 15 0 18"/></svg>
      </span>
      <span class="icon" aria-label="Social profile">
        <svg width="16" height="16" viewBox="0 0 24 24" fill="none" stroke="#fcf3cc" stroke-width="2"><circle cx="12" cy="8" r="4"/><path d="M4 21c0-4.4 3.6-7 8-7s8 2.6 8 7"/></svg>
      </span>
      <span class="icon" aria-label="Social page">
        <svg width="16" height="16" viewBox="0 0 24 24" fill="none" stroke="#fcf3cc" stroke-width="2"><path d="M4 5h16v11H9l-5 4z" stroke-linejoin="round"/></svg>
      </span>
      <span class="rule"></span>
    </div>

    <ul class="contacts">
      <li>555-014-2200</li>
      <li>hello@velourlounge.com</li>
      <li>www.velourlounge.com</li>
      <li>velourlounge.com</li>
      <li>velourlounge.com</li>
    </ul>

    <div class="divider"></div>
    <address class="address">Your address, city<br>state, ZIP 0000</address>
  </section>

  <section class="card card-back" aria-label="Card back">
    <div class="back-seal">
      <span class="brand-name">Velour<br>Lounge</span>
    </div>
  </section>
</main>
</body>
</html>
```